Korean Homemade food restaurant just like what your mom cooks at home

I need a black and white simple and modern design according to my logo.
My restaurant name is Noru Kan (meaning of home cooking).
I need to have 솔찬(Noru Kan) in Korean need to be included. Once again 솔찬.
I am not sure if I need to include my name and number and adress.

솔찬 Noru Kan 418 Marlow Ct. Clarksville, TN 37512 Grant Oh Owner Cell:931-555-0183 Store:931-555-0297

Target Market(s)

business owners, university students

Industry/Entity Type

Restaurant

Contact Information for Business Card

This is traditional Korean food restaurant that targets university students during lunch and Korean business travelers at dinner.

Font styles to use
Sans Serif

Requirements
Must have
• Must have my logo.

```html
<!DOCTYPE html>
<html lang="en">
<head>
<meta charset="utf-8">
<title>Noru Kan — Business Card</title>
<link rel="stylesheet" href="https://fonts.googleapis.com/css2?family=Arimo:wght@400;700&family=Noto+Sans+KR:wght@400;700&display=swap">
<style>
  :root {
    --backdrop: #3a3330;
    --card: #121212;
    --card-edge: #1c1c1c;
    --ink: #ffffff;
    --ink-soft: #d9d9d9;
    --foil: #bdbdbd;
  }
  * { margin: 0; padding: 0; box-sizing: border-box; }
  html, body {
    width: 1200px;
    height: 780px;
    overflow: hidden;
    background: var(--backdrop);
    font-family: "Arimo", "Noto Sans KR", Arial, sans-serif;
  }
  .stage {
    position: relative;
    width: 1200px;
    height: 780px;
    display: flex;
    align-items: center;
    justify-content: center;
    gap: 50px;
  }
  .card {
    position: relative;
    width: 540px;
    height: 310px;
    background: var(--card);
    border: 1px solid var(--card-edge);
    border-radius: 4px;
    box-shadow: 0 10px 28px rgba(0, 0, 0, 0.45);
    color: var(--ink);
  }

  /* Front */
  .card-front {
    display: flex;
    flex-direction: column;
    align-items: center;
    justify-content: center;
    gap: 10px;
  }
  .brand-front {
    display: flex;
    align-items: center;
    gap: 16px;
    color: var(--foil);
  }
  .brand-dot {
    width: 26px;
    height: 26px;
    border-radius: 50%;
    background: var(--foil);
  }
  .brand-front .brand-name {
    font-size: 54px;
    font-weight: 700;
    letter-spacing: -0.5px;
  }
  .brand-korean {
    font-family: "Noto Sans KR", sans-serif;
    font-weight: 700;
    color: var(--foil);
  }
  .card-front .brand-korean {
    font-size: 26px;
    letter-spacing: 4px;
    padding-left: 42px;
  }

  /* Back */
  .brand-back {
    position: absolute;
    top: 36px;
    left: 0;
    right: 0;
    text-align: center;
    font-size: 34px;
    font-weight: 700;
    line-height: 1.1;
    color: var(--ink);
  }
  .card-back .brand-korean {
    display: block;
    margin-top: 4px;
    font-size: 18px;
    letter-spacing: 3px;
    color: var(--ink-soft);
  }
  .person {
    position: absolute;
    top: 132px;
    left: 0;
    right: 0;
    text-align: center;
  }
  .person-name {
    font-size: 22px;
    font-weight: 400;
  }
  .person-name strong { font-weight: 700; }
  .person-role {
    margin-top: 4px;
    font-size: 11px;
    color: var(--ink-soft);
  }
  .address {
    position: absolute;
    top: 206px;
    right: 290px;
    text-align: right;
    font-size: 15px;
    font-style: normal;
    line-height: 1.4;
  }
  .divider {
    position: absolute;
    top: 228px;
    left: 270px;
    width: 1px;
    height: 36px;
    background: var(--ink);
  }
  .phones {
    position: absolute;
    top: 234px;
    left: 292px;
    list-style: none;
    font-size: 16px;
    line-height: 1.45;
  }
  .phones li {
    display: flex;
    align-items: center;
    gap: 8px;
  }
  .phone-icon {
    width: 14px;
    height: 14px;
    flex: none;
  }
</style>
</head>
<body>
  <main class="stage">
    <section class="card card-front" aria-label="Card front">
      <div class="brand-front">
        <span class="brand-dot"></span>
        <span class="brand-name">Noru Kan</span>
      </div>
      <span class="brand-korean" lang="ko">솔찬</span>
    </section>

    <section class="card card-back" aria-label="Card back">
      <div class="brand-back">
        Noru Kan
        <span class="brand-korean" lang="ko">솔찬</span>
      </div>
      <div class="person">
        <p class="person-name">Grant <strong>Oh</strong></p>
        <p class="person-role">Owner</p>
      </div>
      <address class="address">
        418 Marlow Ct.<br>
        Clarksville, TN 37512
      </address>
      <span class="divider"></span>
      <ul class="phones">
        <li>
          <svg class="phone-icon" viewBox="0 0 14 14" aria-hidden="true">
            <rect width="14" height="14" rx="3" fill="#fff"/>
            <rect x="4.5" y="2.5" width="5" height="9" rx="1" fill="#121212"/>
            <rect x="5.5" y="3.8" width="3" height="5" fill="#fff"/>
          </svg>
          <span>931-555-0183</span>
        </li>
        <li>
          <svg class="phone-icon" viewBox="0 0 14 14" aria-hidden="true">
            <rect width="14" height="14" rx="3" fill="#fff"/>
            <path d="M3 5.2c0-1 1-1.7 4-1.7s4 .7 4 1.7v.8H9V5H5v1H3z" fill="#121212"/>
            <rect x="3.5" y="7" width="7" height="4" rx="1" fill="#121212"/>
          </svg>
          <span>931-555-0297</span>
        </li>
      </ul>
    </section>
  </main>
</body>
</html>
```